Bright Oak Fitness Facility Business Cards

Business Card Design that incorporates the logo and tagline

Target Market(s)

Fitness, People Who Exercise

Contact Information for Business Card

2817 Mossgrove Bend Road
Harlow Springs, Oregon 97412
Phone: 541-555-Jump (5867)
www.brightoakfitness.example
info@brightoakfitness.example

Requirements
Must have
• Logo, Address, Website, email and tagline "Stronger Every Day". Colors should be red/black/grey/white

```html
<!DOCTYPE html>
<html lang="en">
<head>
<meta charset="utf-8">
<title>Bright Oak Fitness – Business Cards</title>
<link rel="stylesheet" href="https://fonts.googleapis.com/css2?family=Roboto:wght@400;500;700&display=swap">
<style>
  :root {
    --page: #1d1d1e;
    --card-dark: #1a1a1b;
    --card-light: #f0f0f0;
    --red: #e3232b;
    --grey: #b9b9b9;
    --silver: #9a9a9a;
    --ink: #1c1c1c;
    --white: #f4f4f4;
  }
  * { margin: 0; padding: 0; box-sizing: border-box; }
  html, body {
    width: 1200px; height: 986px; overflow: hidden;
    background: var(--page);
    font-family: "Roboto", Arial, sans-serif;
  }
  .card {
    position: absolute; left: 342px;
    width: 516px; height: 296px;
    border-radius: 28px; overflow: hidden;
    background: var(--card-dark);
  }
  .card-front { top: 160px; }
  .card-back { top: 530px; }
  .front-shape { position: absolute; inset: 0; }
  .contact { position: absolute; left: 34px; top: 0; color: var(--white); }
  .contact-name {
    position: absolute; top: 71px; left: 0; white-space: nowrap;
    font-size: 24px; font-weight: 700; color: var(--red);
  }
  .contact-title { position: absolute; top: 100px; left: 0; font-size: 16px; }
  .address { position: absolute; top: 143px; left: 0; font-size: 12.5px; line-height: 18px; white-space: nowrap; }
  .links { position: absolute; top: 197px; left: 0; list-style: none; font-size: 12.5px; line-height: 17.6px; white-space: nowrap; }
  .links li { display: flex; align-items: center; gap: 6px; }
  .links svg { width: 10px; height: 10px; }
  .icon-fill { fill: var(--red); }
  .icon-line { fill: none; stroke: var(--red); stroke-width: 1; }
  .brand-front {
    position: absolute; left: 264px; width: 240px; top: 128px;
    text-align: center; color: var(--ink);
  }
  .brand-dot { width: 18px; height: 18px; border-radius: 50%; background: var(--red); margin: 0 auto 14px; }
  .brand-name { font-size: 20px; font-weight: 500; letter-spacing: 0.4px; white-space: nowrap; }
  .brand-rule { width: 176px; height: 2px; margin: 6px auto 0; background: var(--ink); }
  .brand-back {
    position: absolute; left: 0; right: 0; top: 130px;
    text-align: center; color: var(--silver);
  }
  .brand-back .brand-dot { background: var(--grey); }
  .brand-back .brand-name { font-size: 26px; }
  .brand-back .brand-rule { width: 230px; height: 1px; background: var(--silver); }
  .tagline {
    position: absolute; top: 250px; left: 106px; width: 304px;
    display: flex; align-items: center; gap: 10px;
    color: var(--white); font-size: 12px; white-space: nowrap;
  }
  .tagline::before, .tagline::after {
    content: ""; flex: 1; height: 2px;
    background: linear-gradient(90deg, transparent, var(--red) 60%);
  }
  .tagline::after { background: linear-gradient(90deg, var(--red) 40%, transparent); }
</style>
</head>
<body>
  <section class="card card-front">
    <svg class="front-shape" viewBox="0 0 516 296" aria-hidden="true">
      <defs>
        <linearGradient id="bevel" x1="0" y1="0" x2="1" y2="0">
          <stop offset="0" stop-color="#8f8f8f"/>
          <stop offset="0.5" stop-color="#d6d6d6"/>
        </linearGradient>
      </defs>
      <circle cx="412" cy="148" r="180" fill="url(#bevel)"/>
      <circle cx="416" cy="148" r="170" fill="#e3232b"/>
      <circle cx="420" cy="148" r="168" fill="#f0f0f0"/>
      <rect x="420" y="0" width="96" height="296" fill="#f0f0f0"/>
    </svg>
    <div class="contact">
      <h1 class="contact-name">Marcus T. Hale</h1>
      <p class="contact-title">Director</p>
      <p class="address">2817 Mossgrove Bend Road<br>Harlow Springs, Oregon 97412</p>
      <ul class="links">
        <li><svg viewBox="0 0 10 10"><path class="icon-fill" d="M2 0.5 3.6 2.6 2.8 3.8Q4 6.2 6.2 7.2L7.4 6.4 9.5 8 8.4 9.6Q3.6 9 0.4 1.6Z"/></svg>541-555-Jump (5867)</li>
        <li><svg viewBox="0 0 10 10"><path class="icon-fill" d="M0 1.5H10V3L5 6 0 3Z M0 4.2 5 7.2 10 4.2V8.5H0Z"/></svg>info@brightoakfitness.example</li>
        <li><svg viewBox="0 0 10 10"><g class="icon-line"><circle cx="5" cy="5" r="4.4"/><ellipse cx="5" cy="5" rx="1.9" ry="4.4"/><path d="M0.6 5H9.4M1.4 2.8H8.6M1.4 7.2H8.6"/></g></svg>www.brightoakfitness.example</li>
      </ul>
    </div>
    <div class="brand-front">
      <div class="brand-dot"></div>
      <p class="brand-name">BRIGHT OAK FITNESS</p>
      <div class="brand-rule"></div>
    </div>
  </section>

  <section class="card card-back">
    <div class="brand-back">
      <div class="brand-dot"></div>
      <p class="brand-name">BRIGHT OAK FITNESS</p>
      <div class="brand-rule"></div>
    </div>
    <p class="tagline">STRONGER EVERY DAY</p>
  </section>
</body>
</html>
```